Larkspur Ridge Management - Business Cards

I need business cards. My current logo was designed by a designer at this site and I very much like and am happy with the results. I would like a business card that is trendy, unique, current yet professional. I deal with high net worth clients daily

Target Market(s)

Out of state investors looking to get into the rental market in Ohio

Industry/Entity Type

Property Management, Consulting

Contact Information for Business Card

Name, Title (Chief Financial Officer) office phone number (555) 817-3094 website address larkridgemgmt.example

Font styles to use
Sans Serif

Colors
0054AA
0677BA
7BADD7
CADEEF
E8F1F8
0094D4
00A9DD
6FCCEA
C7EBF8
E9F6FB
00AB8E
00BBA5
67D7C9
C6EFE9
E9F9F6

```html
<!DOCTYPE html>
<html lang="en">
<head>
<meta charset="utf-8">
<title>Larkspur Ridge Management – Business Cards</title>
<link href="https://fonts.googleapis.com/css2?family=Montserrat:wght@400;500;700;800&display=swap" rel="stylesheet">
<style>
  :root {
    --brand-blue: #0054AA;
    --mid-blue: #0677BA;
    --sky: #7BADD7;
    --mist: #E8F1F8;
    --teal: #00AB8E;
    --teal-light: #67D7C9;
    --white: #ffffff;
    --backdrop: #e9ecef;
  }
  * { margin: 0; padding: 0; box-sizing: border-box; }
  html, body {
    width: 1200px; height: 670px; overflow: hidden;
    background: var(--backdrop);
    font-family: "Montserrat", sans-serif;
  }
  .sheet {
    position: relative; width: 1200px; height: 670px;
    display: flex; align-items: center; justify-content: center; gap: 50px;
  }
  .card {
    position: relative; width: 520px; height: 298px;
    box-shadow: 0 6px 18px rgba(0,0,0,0.12);
    border-bottom: 5px solid var(--teal);
  }
  /* Front */
  .card-front { background: var(--white); }
  .card-front .frame {
    position: absolute; inset: 16px;
    border: 3px solid var(--brand-blue);
  }
  .card-front .frame-inner {
    position: absolute; inset: 24px;
    border: 1.5px solid var(--brand-blue);
  }
  .brand {
    position: absolute; inset: 0;
    display: flex; align-items: center; justify-content: center; gap: 18px;
  }
  .brand-mark { width: 40px; height: 40px; background: var(--teal); flex: none; }
  .brand-name {
    color: var(--brand-blue); font-weight: 800; font-size: 30px;
    text-transform: uppercase; letter-spacing: 0.02em; line-height: 1.12;
    max-width: 340px;
  }
  /* Back */
  .card-back {
    background: var(--brand-blue); color: var(--white);
    display: flex; flex-direction: column; align-items: center; justify-content: center;
    text-align: center;
  }
  .person-name {
    font-weight: 800; font-size: 32px; letter-spacing: 0.06em; text-transform: uppercase;
  }
  .person-title {
    color: var(--teal-light); font-weight: 500; font-size: 14px; letter-spacing: 0.09em;
    text-transform: uppercase; margin-top: 4px;
  }
  .contact { margin-top: 22px; font-size: 19px; font-weight: 400; line-height: 1.4; letter-spacing: 0.02em; }
  .contact .label { font-weight: 700; }
  .accent { margin-top: 18px; display: block; }
</style>
</head>
<body>
  <main class="sheet">
    <section class="card card-front" aria-label="Business card front">
      <div class="frame"></div>
      <div class="frame-inner"></div>
      <div class="brand">
        <span class="brand-mark"></span>
        <span class="brand-name">Larkspur Ridge Management</span>
      </div>
    </section>

    <section class="card card-back" aria-label="Business card back">
      <h1 class="person-name">Daniel Marsh</h1>
      <p class="person-title">Chief Financial Officer</p>
      <p class="contact">
        <span class="label">p:</span> (555) 817-3094<br>
        <span class="label">w:</span> larkridgemgmt.example
      </p>
      <svg class="accent" width="26" height="16" viewBox="0 0 26 16" aria-hidden="true">
        <polygon points="13,0 26,16 0,16" fill="#00AB8E"/>
      </svg>
    </section>
  </main>
</body>
</html>
```